redesign my woocommerce store to a minimalist and modern feel

Hi,i have a store that i quickly put together without much thought for design, here it is venrok( )plo( )ta(.) com i just knew i wanted something simple and minimalistic, our different type of logo is attached, having said that i want a complete redesign the homepage, product page, cart page, and the checkout/payment page, i want something modern and simple, i quite like how our products are displayed currently with the pictures in the homepage but that's about it, everything else is up to you.so just to recap. here is my most important conditions: the design should be minimalist, the design should support Arabic and English

Target Market(s)

Gamers

Industry/Entity Type

Games

Number of Pages Required

4 page

Font styles to use
Sans Serif

Colors

Designer to choose colors to be used in the design.

Requirements
Must have
• Simple and minimalist
• has to support 2 languages, so a drop down or a language switcher should be included in the design
Should not have
• crowded design

```html
<!DOCTYPE html>
<html lang="en">
<head>
<meta charset="utf-8">
<title>Nuvo – Game Coins Store</title>
<link href="https://fonts.googleapis.com/css2?family=Montserrat:wght@500;600;700;800;900&family=Open+Sans:wght@400;600&display=swap" rel="stylesheet">
<style>
:root{
  --orange:#e9531d;
  --ink:#1e1e1e;
  --text:#555555;
  --muted:#8a8a8a;
  --soft:#f4f1f1;
  --line:#dcdcdc;
  --white:#ffffff;
  --coin:#f4c21c;
}
*{margin:0;padding:0;box-sizing:border-box}
html,body{width:1200px;height:3488px;overflow:hidden;background:var(--white)}
body{position:relative;font-family:'Open Sans',Arial,sans-serif;color:var(--text)}
.abs{position:absolute}
.heading{font-family:'Montserrat',Arial,sans-serif;font-weight:800;color:var(--ink)}
.btn{position:absolute;background:var(--orange);color:var(--white);font-family:'Montserrat',Arial,sans-serif;font-weight:700;font-size:13px;display:flex;align-items:center;justify-content:center;letter-spacing:.3px;border-radius:2px}
.brand{font-family:'Montserrat',Arial,sans-serif;font-weight:900;color:var(--orange);letter-spacing:-3px}

/* header + hero */
.hero{position:absolute;left:0;top:0;width:1200px;height:692px;background:var(--soft)}
.hero .brand{left:128px;top:18px;font-size:96px;line-height:1}
.search{left:582px;top:34px;width:228px;height:26px;border:1px solid #bdbdbd;background:var(--white);font-size:10px;padding:6px 8px;color:#666}
.search svg{position:absolute;right:8px;top:7px}
.cart{left:842px;top:32px;display:flex;gap:8px;align-items:center}
.cart .bag{width:24px;height:28px;background:#e35a2a;border-radius:3px}
.cart .label{font-family:'Montserrat',sans-serif;font-size:9px;font-weight:700;color:var(--ink);line-height:1.2}
.cart .label b{display:block;color:var(--orange);font-size:15px}
.lang{left:957px;top:34px;width:108px;height:26px;border:1px solid #bdbdbd;background:var(--white);font-size:9px;display:flex;align-items:center;gap:6px;padding:0 8px;color:#333}
.lang .flag{width:14px;height:9px;background:#3a4a8a}
.nav{left:580px;top:91px;display:flex;gap:27px;font-family:'Montserrat',sans-serif;font-size:12px;font-weight:700;color:var(--ink)}
.nav .active{color:var(--orange)}
.hero-title{left:130px;top:312px;font-size:46px;line-height:1.1;font-weight:900}
.hero-title span{color:var(--orange)}
.hero-art{left:430px;top:150px;width:700px;height:530px;border-radius:30px;background:radial-gradient(ellipse at 55% 60%,#f5b48f 0%,#e9d9d4 55%,var(--soft) 80%)}

/* products */
.section-title{position:absolute;left:0;width:1200px;text-align:center;font-size:25px}
.rule{position:absolute;left:578px;width:44px;height:3px;background:#b9b9b9}
.card{position:absolute;top:895px;width:226px;height:333px;background:var(--white);box-shadow:0 4px 14px rgba(0,0,0,.14);text-align:center}
.card .top{height:135px;background:var(--soft);border-radius:0 0 50% 50%/0 0 30px 30px;display:flex;align-items:center;justify-content:center}
.card .mark{font-family:'Montserrat',sans-serif;font-weight:800;font-size:34px}
.card h3{font-family:'Montserrat',sans-serif;font-weight:700;font-size:16px;color:var(--ink);margin-top:38px}
.card p{font-size:14px;color:var(--ink);margin-top:12px;line-height:1.35}
.card p b{color:var(--orange);font-size:17px}
.card .btn{left:63px;bottom:38px;width:100px;height:26px}

/* features */
.features{position:absolute;left:0;top:1330px;width:1200px;height:685px;background:var(--soft)}
.feat{position:absolute;width:270px}
.feat h4{font-family:'Montserrat',sans-serif;font-size:15px;font-weight:800;color:var(--ink);line-height:1.2;margin-bottom:8px}
.feat p{font-size:12px;line-height:1.45;color:var(--text)}
.feat-icon{position:absolute;width:62px;height:62px;border-radius:50%;background:var(--orange);display:flex;align-items:center;justify-content:center}
.feat-sep{position:absolute;height:1px;background:var(--line);width:270px}
.coins-art{left:450px;top:1470px;width:245px;height:480px;border-radius:120px;background:linear-gradient(180deg,rgba(244,194,28,.15),#f7cf43 45%,#eeb314)}

/* welcome */
.welcome-blob{left:0;top:2050px;width:720px;height:700px;background:var(--soft);border-radius:0 60% 45% 0/0 55% 45% 0}
.welcome-art{left:100px;top:2140px;width:540px;height:530px;border-radius:40px;background:radial-gradient(ellipse at 45% 70%,#5ab43c 0%,#9fcf86 35%,rgba(244,241,241,0) 75%)}
.welcome-title{left:722px;top:2335px;font-size:25px}
.welcome-rule{left:722px;top:2374px;width:134px;height:3px;background:var(--orange)}
.welcome-text{left:722px;top:2420px;width:425px;font-size:13.5px;line-height:1.65;color:var(--text)}

/* payments */
.pay-line{position:absolute;left:130px;width:940px;height:1px;background:var(--line)}
.pays{position:absolute;left:130px;top:2818px;width:940px;display:flex;justify-content:space-around;align-items:center;font-family:'Montserrat',sans-serif;font-weight:800;font-size:26px}

/* footer */
.footer-bg{left:0;top:2990px;width:1200px;height:498px}
.footer .brand{left:128px;top:3170px;font-size:100px;line-height:1}
.fcol{position:absolute;top:3183px;font-size:12px;color:#333;line-height:1.5}
.fcol h5{font-family:'Montserrat',sans-serif;font-size:12px;font-weight:800;color:var(--ink);margin-bottom:22px}
.frow{display:flex;gap:14px;align-items:flex-start;margin-bottom:18px}
.menu li{list-style:none;line-height:1.45}
.email{width:178px;height:36px;border:1px solid #555;background:var(--white);font-size:11px;padding:10px 12px;color:#666}
.social{display:flex;align-items:center;gap:10px;margin-bottom:14px}
.social i{width:24px;height:24px;border-radius:50%;display:block}
.copy{position:absolute;left:0;top:3445px;width:1200px;text-align:center;font-size:11px;color:#333}
</style>
</head>
<body>

<!-- Header and hero -->
<section class="hero">
  <div class="abs brand">Nuvo</div>
  <div class="abs search">SEARCH
    <svg width="11" height="11" viewBox="0 0 12 12"><circle cx="5" cy="5" r="3.8" fill="none" stroke="#666" stroke-width="1.4"/><line x1="8" y1="8" x2="11" y2="11" stroke="#666" stroke-width="1.4"/></svg>
  </div>
  <div class="abs cart"><div class="bag"></div><div class="label">MY CART<b>$0.00</b></div></div>
  <div class="abs lang"><span class="flag"></span>ENGLISH <span style="margin-left:auto">▾</span></div>
  <nav class="abs nav"><span class="active">HOME</span><span>ABOUT US</span><span>SERVICES</span><span>GAMES</span><span>BLOG</span><span>CONTACT US</span></nav>
  <h1 class="abs heading hero-title">SUITS YOUR<br><span>MOOD</span></h1>
  <a class="btn" style="left:130px;top:438px;width:130px;height:38px">READ MORE</a>
  <div class="abs hero-art" role="img" aria-label="Illustration of a father and son gaming together on a red sofa, with floating gold coins, a window, plant and wall clock"></div>
</section>

<!-- Products -->
<h2 class="heading section-title" style="top:762px">PRODUCTS</h2>
<div class="rule" style="top:810px"></div>

<article class="card" style="left:130px">
  <div class="top"><span class="mark" style="color:#2aa3d8">Lumi</span></div>
  <h3>LUMI</h3><p>Buy 10 coins<br>for <b>$40</b></p><a class="btn">BUY NOW</a>
</article>
<article class="card" style="left:367px">
  <div class="top"><span class="mark" style="color:#c23bb4">Tavo</span></div>
  <h3>TAVO</h3><p>Buy 10 coins<br>for <b>$40</b></p><a class="btn">BUY NOW</a>
</article>
<article class="card" style="left:604px">
  <div class="top"><span class="mark" style="color:#8a4a12">Ravek</span></div>
  <h3>RAVEK</h3><p>Buy 10 coins<br>for <b>$40</b></p><a class="btn">BUY NOW</a>
</article>
<article class="card" style="left:841px">
  <div class="top"><span class="mark" style="color:#7a1a5a">Zibbo</span></div>
  <h3>ZIBBO</h3><p>Buy 10 coins<br>for <b>$40</b></p><a class="btn">BUY NOW</a>
</article>

<!-- Features -->
<section class="features"></section>
<h2 class="heading section-title" style="top:1402px">FEATURES</h2>
<div class="rule" style="top:1450px"></div>
<div class="abs coins-art" role="img" aria-label="Illustration of a cascade of shining gold star coins"></div>

<div class="feat-icon" style="left:130px;top:1555px"><svg width="28" height="28" viewBox="0 0 28 28" fill="none" stroke="#fff" stroke-width="2"><ellipse cx="12" cy="8" rx="8" ry="3"/><path d="M4 8v5c0 1.7 3.6 3 8 3s8-1.3 8-3V8M4 13v5c0 1.7 3.6 3 8 3s8-1.3 8-3v-5"/></svg></div>
<div class="feat" style="left:214px;top:1550px"><h4>EXCHANGING COINS</h4><p>Sed ut perspiciatis unde omnis iste natus error sit volu ptatem accusant ium doloremque laudantium.</p></div>
<div class="feat-sep" style="left:130px;top:1652px"></div>

<div class="feat-icon" style="left:130px;top:1677px"><svg width="28" height="28" viewBox="0 0 24 24"><path fill="#fff" d="M12 2l3 6.5 7 .8-5.2 4.8 1.4 7L12 17.6 5.8 21l1.4-7L2 9.3l7-.8z"/></svg></div>
<div class="feat" style="left:214px;top:1672px"><h4>AUTOMATED LOYALTY<br>REWARDS</h4><p>Sed ut perspiciatis unde omnis iste natus error sit volu ptatem accusant ium doloremque laudantium.</p></div>
<div class="feat-sep" style="left:130px;top:1795px"></div>

<div class="feat-icon" style="left:130px;top:1825px"><svg width="26" height="28" viewBox="0 0 24 26" fill="none" stroke="#fff" stroke-width="2.2"><rect x="4" y="11" width="16" height="12" rx="2"/><path d="M8 11V7a4 4 0 0 1 8 0"/></svg></div>
<div class="feat" style="left:214px;top:1818px"><h4>NEW WAY OF<br>UNLOCKING LEVELS</h4><p>Sed ut perspiciatis unde omnis iste natus error sit volu ptatem accusant ium doloremque laudantium.</p></div>

<div class="feat" style="left:780px;top:1543px"><h4>DISCOUNTED IN-GAME<br>PURCHASE</h4><p>Sed ut perspiciatis unde omnis iste natus error sit volu ptatem.</p></div>
<div class="feat-icon" style="left:1005px;top:1555px"><svg width="28" height="28" viewBox="0 0 24 24" fill="none" stroke="#fff" stroke-width="2.2"><line x1="5" y1="19" x2="19" y2="5"/><circle cx="7" cy="7" r="2.5"/><circle cx="17" cy="17" r="2.5"/></svg></div>
<div class="feat-sep" style="left:780px;top:1652px;width:285px"></div>

<div class="feat" style="left:780px;top:1672px"><h4>EASY ADD-ON</h4><p>Sed ut perspiciatis unde omnis iste natus error sit volu ptatem accusant ium doloremque laudantium.</p></div>
<div class="feat-icon" style="left:1005px;top:1677px"><svg width="30" height="30" viewBox="0 0 24 24" fill="none" stroke="#fff" stroke-width="2.4"><circle cx="12" cy="12" r="9"/><line x1="12" y1="7" x2="12" y2="17"/><line x1="7" y1="12" x2="17" y2="12"/></svg></div>
<div class="feat-sep" style="left:780px;top:1795px;width:285px"></div>

<div class="feat" style="left:780px;top:1818px"><h4>SECURE TRANSACTIONS</h4><p>Sed ut perspiciatis unde omnis iste natus error sit volu ptatem accusant ium doloremque laudantium.</p></div>
<div class="feat-icon" style="left:1005px;top:1825px"><svg width="30" height="26" viewBox="0 0 26 22" fill="none" stroke="#fff" stroke-width="2"><rect x="2" y="4" width="22" height="15" rx="2"/><line x1="2" y1="9" x2="24" y2="9"/><line x1="6" y1="14" x2="12" y2="14"/></svg></div>

<!-- Welcome -->
<div class="abs welcome-blob"></div>
<div class="abs welcome-art" role="img" aria-label="Illustration of a bearded man playing a video game on a green sofa beside a lamp, with gold coins floating above"></div>
<h2 class="abs heading welcome-title">WELCOME TO OUR SITE</h2>
<div class="abs welcome-rule"></div>
<p class="abs welcome-text">Sed ut perspiciatis unde omnis iste natus error sit volu ptatem accusantium doloremque laudantium, totam rem aperiam, eaque ipsa quae ab illo inventore veritatis et quasi architecto beatae vitae dicta sunt explicabo. Nemo enim ipsam voluptatem quia voluptas sit aspernatur aut odit aut fugit</p>
<a class="btn" style="left:722px;top:2575px;width:114px;height:30px">READ MORE</a>

<!-- Payment methods -->
<div class="pay-line" style="top:2793px"></div>
<div class="pays">
  <span style="color:#1a3a8a">Payline</span>
  <span style="color:#d8332a">Cardora</span>
  <span style="color:#2a7ab0">Nexa</span>
  <span style="color:#e06a2a">Sadira</span>
</div>
<div class="pay-line" style="top:2895px"></div>

<!-- Footer -->
<footer class="footer">
  <svg class="abs footer-bg" viewBox="0 0 1200 498" preserveAspectRatio="none"><path d="M0 60 C200 0 380 80 600 40 C820 0 1000 70 1200 30 L1200 498 L0 498 Z" fill="#f4f3f3"/><path d="M0 110 C260 60 420 130 640 90 C860 50 1020 110 1200 80 L1200 498 L0 498 Z" fill="#f8f7f7"/></svg>
  <div class="abs brand">Nuvo</div>

  <div class="fcol" style="left:404px"><h5>CONTACT US</h5>
    <div class="frow"><svg width="10" height="14" viewBox="0 0 10 14"><path d="M5 0a5 5 0 0 0-5 5c0 4 5 9 5 9s5-5 5-9a5 5 0 0 0-5-5z" fill="#333"/><circle cx="5" cy="5" r="1.8" fill="#fff"/></svg><span>88 Harbor Lane<br>Westfield, OR 97001</span></div>
    <div class="frow"><svg width="12" height="12" viewBox="0 0 24 24"><path fill="#333" d="M6.6 10.8a15 15 0 0 0 6.6 6.6l2.2-2.2c.3-.3.7-.4 1-.2 1.1.4 2.3.6 3.6.6.6 0 1 .4 1 1V20c0 .6-.4 1-1 1A17 17 0 0 1 3 4c0-.6.4-1 1-1h3.5c.6 0 1 .4 1 1 0 1.3.2 2.5.6 3.6.1.3 0 .7-.2 1z"/></svg><span>555.010.2040</span></div>
    <div class="frow"><svg width="13" height="10" viewBox="0 0 13 10"><rect width="13" height="10" fill="#333"/><path d="M0 0l6.5 5L13 0" stroke="#fff" fill="none"/></svg><span>info@venrokplota.com</span></div>
  </div>

  <div class="fcol" style="left:597px"><h5>MENU</h5>
    <ul class="menu"><li>HOME</li><li>ABOUT US</li><li>SERVICES</li><li>GAMES</li><li>BLOG</li><li>CONTACT US</li></ul>
  </div>

  <div class="fcol" style="left:718px"><h5>NEWSLETTER</h5>
    <div class="email">E mail id</div>
    <a class="btn" style="position:relative;width:72px;height:28px;margin-top:22px;font-size:12px">SIGNUP</a>
  </div>

  <div class="fcol" style="left:936px"><h5>CONNECT WITH US</h5>
    <div class="social"><i style="background:#3b5998"></i>Chatterly</div>
    <div class="social"><i style="background:#1da1f2"></i>Flockit</div>
    <div class="social"><i style="background:#1a2a5a"></i>Linkwise</div>
  </div>

  <div class="pay-line" style="top:3402px;background:#cfcfcf"></div>
  <p class="copy">Copyrights @ 2018 All Rights Reserved</p>
</footer>

</body>
</html>
```